Label for Skincare Brand

"Fernbrook Organics" - organic skincare brand
I need a label designed for my organic skincare brand. I have attached pics of brands I like, to give you an idea of style. I would like something minimal although some colour might work. Colours I like are pale blush pink and aqua. I would like a clean, minimalistic modern yet elegant label. Please look at the samples because they demonstrate the style I look for in a label. It is okay to add a graphical element into the design as long as it enhances or add value to the design.
We do not have a logo yet, so I'd appreciate if you could create a simple type logo for Fernbrook Organics similar to the examples attached.
Please can you do two different sizes: one cream jar and one serum bottle. Both will contain the same information.
___________________________________________________
1. Cream Jar (label size 42 x 190 mm) (clear glass with aluminium lid)
2. Serum Bottle (label size 50 x 110 mm) (clear glass with black pump)
FRONT SIDE:
Fernbrook Organics
Moonpetal
Ultimate Anti-Aging Cream
For Dry & Mature Skin
Organic & Palm Oil-Free
100 ml.
BACK SIDE:
Moonpetal Radiance Renewal Cream
An effective Day Cream that harnesses the best of science to target the signs of aging. The main active ingredient is K7M, a patented noncomedogenic lipid complex, carefully engineered from botanically-sourced lipids. It is composed of a variety of lipid types which are carefully combined in the same ratio as those found on healthy young skin of an average 22 year old.
Directions:
Apply to clean skin morning and night.
Ingredients:
Aloe Vera Leaf Juice, Cocos Nucifera Oil, Butyrospermum Parkii Butter, Jojoba Oil/Macadamia Seed Oil Esters (and) Squalene (and) Phytosteryl Macadamiate (and) Phytosterols, Potassium Olivoyl Hydrolyzed Oat Protein (and) Cetearyl Alcohol (and) Glyceryl Oleate (and) Glyceryl Stearat, Benzyl Alcohol, Dehydroacetic Acid.
Fernbrook Organics
5/2 Kellerton Parade West, Larkhaven, NSW 2999
www.fernbrookorganics.example
Any questions, please just ask away. Thank you.

```html
<!DOCTYPE html>
<html lang="en">
<head>
<meta charset="utf-8">
<title>Fernbrook Organics – Moonpetal Cream Jar Label</title>
<link rel="stylesheet" href="https://fonts.googleapis.com/css2?family=Bodoni+Moda:wght@400&family=Montserrat:wght@400;500;600&display=swap">
<style>
  :root {
    --page: #f4f4f4;
    --label: #ffffff;
    --blush: #f3d3cc;
    --blush-deep: #e2a89e;
    --ink: #2f2f2f;
    --ink-soft: #5a4a47;
    --rule: #3a3a3a;
  }
  * { box-sizing: border-box; margin: 0; padding: 0; }
  html, body { width: 1200px; height: 703px; overflow: hidden; }
  body {
    background: var(--page);
    font-family: "Montserrat", sans-serif;
    color: var(--ink);
    position: relative;
  }
  .label {
    position: absolute;
    left: 50px;
    top: 230px;
    width: 1100px;
    height: 243px;
    background: var(--label);
    display: grid;
    grid-template-columns: 250px 1fr 250px;
    box-shadow: 0 1px 3px rgba(0,0,0,0.08);
  }
  .side-panel {
    background: var(--blush);
    margin: 18px 0;
    padding: 14px 16px;
    color: var(--ink-soft);
    font-size: 6.4px;
    line-height: 1.45;
  }
  .side-panel--left { border-radius: 0 10px 10px 0; }
  .side-panel--right { border-radius: 10px 0 0 10px; }
  .side-panel h3 {
    font-size: 7.4px;
    font-weight: 600;
    letter-spacing: 0.04em;
    margin-bottom: 4px;
    text-transform: uppercase;
  }
  .side-panel p + h3 { margin-top: 6px; }
  .side-panel .maker { margin-top: 7px; }
  .front {
    display: flex;
    flex-direction: column;
    align-items: center;
    justify-content: center;
  }
  .brand-name {
    font-size: 14px;
    font-weight: 500;
    letter-spacing: 0.28em;
    text-transform: uppercase;
    color: var(--ink);
    margin-bottom: 20px;
  }
  .product-lockup {
    display: grid;
    grid-template-columns: auto 1px auto;
    column-gap: 14px;
    align-items: center;
  }
  .product-name {
    font-family: "Bodoni Moda", serif;
    font-weight: 400;
    font-size: 60px;
    line-height: 1;
    color: var(--blush-deep);
  }
  .product-rule {
    width: 1px;
    height: 60px;
    background: var(--rule);
  }
  .product-details {
    font-size: 12.5px;
    line-height: 1.25;
    text-transform: uppercase;
  }
  .product-details .title { font-weight: 500; color: var(--ink); }
  .product-details .skin { color: var(--blush-deep); font-weight: 500; }
  .product-details .claim { color: var(--ink); }
  .volume {
    grid-column: 3;
    font-size: 11px;
    letter-spacing: 0.06em;
    margin-top: 12px;
  }
</style>
</head>
<body>
  <section class="label" aria-label="Cream jar label, flat">
    <aside class="side-panel side-panel--left">
      <h3>Moonpetal Radiance Renewal Cream</h3>
      <p>An effective Day Cream that harnesses the best of science to target the signs of aging. The main active ingredient is K7M, a patented noncomedogenic lipid complex, carefully engineered from botanically-sourced lipids. It is composed of a variety of lipid types which are carefully combined in the same ratio as those found on healthy young skin of an average 22 year old.</p>
    </aside>

    <div class="front">
      <div class="brand-name">Fernbrook Organics</div>
      <div class="product-lockup">
        <div class="product-name">Moonpetal</div>
        <div class="product-rule"></div>
        <div class="product-details">
          <div class="title">Ultimate<br>Anti-Aging Cream</div>
          <div class="skin">For Dry &amp; Mature Skin</div>
          <div class="claim">Organic &amp; Palm Oil-Free</div>
        </div>
        <div class="volume">100 ML.</div>
      </div>
    </div>

    <aside class="side-panel side-panel--right">
      <h3>Directions:</h3>
      <p>Apply to clean skin morning and night.</p>
      <h3>Ingredients:</h3>
      <p>Aloe Vera Leaf Juice, Cocos Nucifera Oil, Butyrospermum Parkii Butter, Jojoba Oil/Macadamia Seed Oil Esters (and) Squalene (and) Phytosteryl Macadamiate (and) Phytosterols, Potassium Olivoyl Hydrolyzed Oat Protein (and) Cetearyl Alcohol (and) Glyceryl Oleate (and) Glyceryl Stearat, Benzyl Alcohol, Dehydroacetic Acid.</p>
      <p class="maker">Fernbrook Organics<br>5/2 Kellerton Parade West, Larkhaven, NSW 2999<br>www.fernbrookorganics.example</p>
    </aside>
  </section>
</body>
</html>
```